Redo of existing website www.brontivel.com

I would like it to look like the newer style website, with large images, less text. clean and modern looking. The new design should focus on call to action. ultimately that's what were looking for.Some features I would like to see we try to do good job of keeping up with our blog, and it is a good source of recent pictures of our work. I like four visitors to get the few pieces they're doing with a national brand or franchise pray. I like to stay far from the idea of a local one-man band with magnetic signs on his truck.
I think that clean beautiful images have the biggest impact. In my opinion most people don't read more than a couple lines of text. The text is more for search engines.
we are currently in the process of revising our logo as well, I will upload those files when I get them.
Please feel free to use content and images from our current website www.brontivel.com. we can purchase professional stock images if needed.
1. large call to action with easy contact form.
2. Blog roll on front page to showcase our recent work.
2. All social connect buttons.
Check out our reviews on zindexa!
My current websites
Www.brontivel.com
https://plus.vorplink.com/593028416627304918735/about
www.chatterbook.com/brontivel
http://www.skimblr.com/blog/curbmarauder
https://chirpfeed.com/Brontivel
websites I like the way they look.
http://postwren.com/
http://www.vendlio.com/
http://www.corvanblacktop.com/
http://www.tarwayguild.org/
http://groundsurfacecrafts.com/
Updates
Hello all,
I have just uploaded some images of our company mascot "Curb Marauder" and our new logo.
Project Deadline Extended
Reason: Death in family. Finally back to work.
Target Market(s)
We have 2 main groups of customers commercial and residential.
Commercial customers are Property owners and managers, operators of multi location business, restaurant, supermarket, banks, and are best source for repeat business
for Residential customers we provide driveway repair and driveway paving services.
for residential customers I would like to encourge the submission or pictures with the inquiry for a quick quote. Residential customers are typically a one time job but are a good source of referrals
I like how this website separates residential and commercial
http://www.glintcoatdirect.com
Industry/Entity Type
Call
Look and feel
Each slider illustrates characteristics of the customer's brand and the style your logo design should communicate.

```html
<!DOCTYPE html>
<html lang="en">
<head>
<meta charset="utf-8">
<title>Brontivel – Asphalt Paving</title>
<link href="https://fonts.googleapis.com/css2?family=Roboto:wght@400;500;700&display=swap" rel="stylesheet">
<style>
:root{
  --yellow:#f2c811;
  --black:#000;
  --dark:#282828;
  --dark-alt:#2f2f2f;
  --text:#fff;
  --muted:#e6e6e6;
  --ink:#222;
}
*{box-sizing:border-box;margin:0;padding:0}
html,body{width:714px;height:1200px;overflow:hidden;background:var(--dark)}
body{font-family:"Roboto",Arial,sans-serif;color:var(--text);position:relative}
.abs{position:absolute}
.top-stripe{left:0;top:0;width:714px;height:4px;background:var(--yellow)}
.header{left:0;top:4px;width:714px;height:58px;background:var(--black)}
.brand-name{left:119px;top:19px;font-weight:700;font-size:18px;line-height:20px;color:var(--yellow)}
.phone{left:488px;top:20px;display:flex;align-items:center;gap:6px;font-weight:700;font-size:12px}
.nav{left:0;top:62px;width:714px;height:20px;background:var(--yellow)}
.nav a{position:absolute;top:0;line-height:20px;font-size:6px;color:var(--ink);text-decoration:none;transform:translateX(-50%)}
.hero{left:0;top:82px;width:714px;height:288px;background:linear-gradient(180deg,#8fa6c9 0%,#5d6f96 35%,#4a5678 70%,#8a7c86 100%)}
.arrow{top:136px}
.dots{top:274px;left:341px;display:flex;gap:3px}
.dots span{width:7px;height:7px;border-radius:50%;background:#fff}
.dots span:first-child{background:var(--yellow)}
.welcome{left:0;top:370px;width:714px;height:144px;background:var(--dark)}
h2{font-size:11.5px;font-weight:700;color:var(--yellow)}
h3{font-size:11px;font-weight:400;color:var(--yellow)}
.welcome h2{position:absolute;left:119px;top:17px}
.welcome p{position:absolute;left:119px;top:38px;width:280px;font-size:5.6px;line-height:11.4px;color:var(--muted)}
.more{color:var(--yellow);text-decoration:none;font-size:5.6px}
.welcome .more{position:absolute;left:119px;top:114px}
.video{left:411px;top:19px;width:184px;height:108px;background:linear-gradient(135deg,#2d3844,#1e2833 60%,#3a4b63)}
.play{left:80px;top:37px}
.services{left:0;top:514px;width:714px;height:208px;background:var(--dark-alt)}
.services h3.title{position:absolute;left:119px;top:8px}
.svc{position:absolute;top:30px;width:147px}
.svc .photo{width:147px;height:96px;border:2px solid var(--yellow);background:linear-gradient(160deg,#6d7f8e,#3e3a36 60%,#7a6a4a)}
.svc h4{font-size:9.5px;font-weight:400;color:var(--yellow);margin-top:12px}
.svc p{font-size:5.6px;line-height:11.2px;color:var(--muted);margin-top:2px;width:150px}
.cta{left:119px;top:738px;width:476px;height:44px;background:var(--black)}
.cta-text{left:0;top:3px;width:435px;height:40px;background:var(--yellow);padding:6px 12px;font-size:8.4px;line-height:14px;color:#fff}
.cta-icon{left:451px;top:15px}
.works h3{position:absolute;left:119px;top:798px}
.work{position:absolute;top:828px;width:112px;height:150px;background:linear-gradient(160deg,#9bb3c9,#7e8e7a 50%,#4f5e3e)}
.work .cap{position:absolute;left:30px;top:105px;width:82px;height:31px;background:var(--yellow);color:var(--ink);font-size:6.4px;line-height:8px;padding:6px 7px}
.contact{left:0;top:1000px;width:714px;height:146px;background:var(--dark-alt)}
.contact .left-title{position:absolute;left:119px;top:15px}
.contact .left-text{position:absolute;left:119px;top:36px;width:158px;font-size:5.6px;line-height:11.4px;color:var(--muted)}
.contact .right-title{position:absolute;left:338px;top:7px}
.field{position:absolute;background:#fff;color:#444;font-size:5.6px;padding:5px}
.submit{position:absolute;left:339px;top:114px;width:237px;height:16px;background:var(--yellow);color:var(--ink);font-size:6.4px;text-align:center;line-height:16px}
.footer{left:0;top:1146px;width:714px;height:54px;background:var(--yellow);color:var(--ink)}
.footer-links{position:absolute;left:119px;top:13px;font-size:5.6px}
.copyright{position:absolute;left:119px;top:31px;font-size:5.6px}
.social{position:absolute;left:530px;top:14px;display:flex;gap:2px}
.social span{width:15px;height:15px;background:#2a5aa5}
.social span:nth-child(2){background:#2aa3df}
.social span:nth-child(3){background:#d6493a}
.social span:nth-child(4){background:#1577b7}
</style>
</head>
<body>
<div class="abs top-stripe"></div>
<header class="abs header">
  <div class="abs brand-name">Brontivel</div>
  <div class="abs phone">
    <svg width="26" height="14" viewBox="0 0 26 14"><path d="M2 5 Q13 -2 24 5 L22 8 L17 6 L17 4 Q13 3 9 4 L9 6 L4 8 Z" fill="#e8511e"/><rect x="7" y="7" width="12" height="6" rx="2" fill="#e8511e"/></svg>
    <span>866 555 0142</span>
  </div>
</header>
<nav class="abs nav">
  <a style="left:139px">Home</a><a style="left:206px">Commercial</a><a style="left:280px">Residential</a><a style="left:350px">About Us</a><a style="left:424px">Free Estimate</a><a style="left:502px">Testimonials</a><a style="left:568px">Blog</a>
</nav>
<section class="abs hero" role="img" aria-label="Worker spreading fresh sealcoat on a wet parking lot">
  <svg class="abs arrow" style="left:30px" width="12" height="18" viewBox="0 0 12 18"><path d="M10 2 L3 9 L10 16" stroke="#f2c811" stroke-width="3" fill="none"/></svg>
  <svg class="abs arrow" style="left:671px" width="12" height="18" viewBox="0 0 12 18"><path d="M2 2 L9 9 L2 16" stroke="#f2c811" stroke-width="3" fill="none"/></svg>
  <div class="abs dots"><span></span><span></span><span></span></div>
</section>
<section class="abs welcome">
  <h2>Welcome To Our Website</h2>
  <p>Brontivel Asphalt Management is a full-service asphalt paving and maintenance contractor serving commercial customers in Rochester and surrounding communities. The company is owned and operated by Dale Varnholt, a veteran of nearly two decades in the paving and construction trades.<br>Harnessing the skills, experience, and resources of a select network of respected local paving companies, Brontivel provides single-source accountability for a complete range of services including asphalt paving, asphalt repair, sealcoating, striping and signage, lot maintenance plans, and snow &amp; ice control.</p>
  <a class="more">Read More +</a>
  <div class="abs video" role="img" aria-label="Video still of a freshly painted accessible parking stall">
    <svg class="abs play" width="26" height="26" viewBox="0 0 26 26"><circle cx="13" cy="13" r="12" fill="#111" stroke="#fff" stroke-width="1.5"/><path d="M10 7 L19 13 L10 19 Z" fill="#fff"/></svg>
  </div>
</section>
<section class="abs services">
  <h3 class="title">Services</h3>
  <div class="svc" style="left:120px"><div class="photo" role="img" aria-label="Crew patching a residential driveway"></div><h4>Residential</h4><p>Perspiciatis unde omnis iste natus error sit voluptatem accusantium doloremque laudantium, totam rem aperiam. Perspiciatis unde omnis iste natus error sit voluptatem accusantium... <a class="more">Read more</a></p></div>
  <div class="svc" style="left:285px"><div class="photo" role="img" aria-label="Workers raking asphalt at a commercial lot"></div><h4>Commercial / Industrial</h4><p>Perspiciatis unde omnis iste natus error sit voluptatem accusantium doloremque laudantium, totam rem aperiam. Perspiciatis unde omnis iste natus error sit voluptatem accusantium... <a class="more">Read more</a></p></div>
  <div class="svc" style="left:448px"><div class="photo" role="img" aria-label="Operator running a yellow paving machine"></div><h4>Electrical Construction</h4><p>Perspiciatis unde omnis iste natus error sit voluptatem accusantium doloremque laudantium, totam rem aperiam. Perspiciatis unde omnis iste natus error sit voluptatem accusantium... <a class="more">Read more</a></p></div>
</section>
<div class="abs cta">
  <div class="abs cta-text">KRV maintains all necessary licenses and insurance to operate within the city of Philadelphia and<br>surrounding municipalities to include a Master Electricians License.</div>
  <svg class="abs cta-icon" width="16" height="16" viewBox="0 0 16 16"><circle cx="8" cy="8" r="8" fill="#fff"/><path d="M8 4 V12 M4 8 H12" stroke="#000" stroke-width="2"/></svg>
</div>
<section class="works">
  <h3>Recent Works</h3>
  <div class="work" style="left:119px" role="img" aria-label="Aerial view of a paved office parking lot"><div class="cap">Medium/High Voltage Underground</div></div>
  <div class="work" style="left:240px" role="img" aria-label="Company sign beside a freshly paved lot"><div class="cap">Cable Splicing and Repair</div></div>
  <div class="work" style="left:362px" role="img" aria-label="Worker operating a paving machine"><div class="cap">Fault Locating and Cable Testing</div></div>
  <div class="work" style="left:483px" role="img" aria-label="Skid steer loader spreading asphalt"><div class="cap">Manpower and Mobilization</div></div>
</section>
<section class="abs contact">
  <h3 class="left-title">Conatct Best In Business</h3>
  <p class="left-text">Perspiciatis unde omnis iste natus error sit voluptatem accusantium doloremque laudantium, totam rem aperiam. Perspiciatis unde omnis iste natus error sit voluptatem accusantiu Perspiciatis unde omnis iste natus error sit voluptatem accusantium doloremque laudantium, totam rem aperiam. Perspiciatis unde omnis iste natus error sit voluptatem accusantium... <a class="more" style="color:#3a3a3a">Read more</a></p>
  <h3 class="right-title">Quick Contact Form</h3>
  <div class="field" style="left:339px;top:30px;width:111px;height:18px">First name</div>
  <div class="field" style="left:463px;top:30px;width:111px;height:18px">Last name</div>
  <div class="field" style="left:339px;top:54px;width:111px;height:19px">Phone</div>
  <div class="field" style="left:463px;top:54px;width:111px;height:19px">Email</div>
  <div class="field" style="left:339px;top:78px;width:237px;height:31px">Message</div>
  <div class="submit">Submit</div>
</section>
<footer class="abs footer">
  <div class="footer-links">Home | About | Practices | People | Events | Contact | Site Map | Privacy Policy</div>
  <div class="copyright">Copyright © 2014 Brontivel. All Rights Reserved</div>
  <div class="social"><span></span><span></span><span></span><span></span></div>
</footer>
</body>
</html>
```